Body therapist needs a business card

I need a card for my business which is teaching trainings in body therapy, the company is called Wexcombe Educational Group. I teach to massage therapists around Australia, South East Asia and the USA. I am attaching my logo which will guide you as to what colours I would like to have you consider. Please consult my website to find out more about what I do. www.corvantela.com.au

My name is Daniel Wexcombe. My phone number is (03) 9417 2608 or 0461753208. email is info@corvantela.com.au

```html
<!DOCTYPE html>
<html lang="en">
<head>
<meta charset="utf-8">
<title>Wexcombe Educational Group – Business Card</title>
<link href="https://fonts.googleapis.com/css2?family=Open+Sans:wght@400;600;800&display=swap" rel="stylesheet">
<style>
  :root {
    --brown: #5a3322;
    --lime: #c9d92c;
    --red: #b01e24;
    --white: #ffffff;
    --ink: #3a2a22;
    --backdrop: #2b2b2b;
  }
  * { margin: 0; padding: 0; box-sizing: border-box; }
  html, body {
    width: 1200px; height: 900px; overflow: hidden;
    background: var(--backdrop);
    font-family: "Open Sans", Arial, sans-serif;
  }
  .canvas { position: relative; width: 1200px; height: 900px; }

  .card {
    position: absolute;
    left: 270px;
    width: 660px;
    height: 377px;
  }

  /* Back side */
  .card--back { top: 40px; background: var(--brown); }
  .back-mark {
    position: absolute; left: 0; right: 0; top: 120px;
    display: flex; align-items: center; justify-content: center; gap: 16px;
  }
  .back-mark__dot {
    width: 34px; height: 34px; border-radius: 50%; background: var(--white);
  }
  .back-mark__name {
    color: var(--white); font-size: 30px; font-weight: 400; letter-spacing: 0.5px;
  }
  .regions {
    position: absolute; right: 60px; bottom: 48px;
    color: var(--white); font-size: 19px; letter-spacing: 0.8px;
    display: flex; align-items: center; gap: 12px;
  }
  .regions__sep { width: 6px; height: 6px; border-radius: 50%; background: var(--lime); }

  /* Front side */
  .card--front { top: 480px; background: var(--white); }
  .brand {
    position: absolute; left: 40px; top: 150px;
    display: flex; align-items: center; gap: 12px;
  }
  .brand__dot { width: 30px; height: 30px; border-radius: 50%; background: var(--brown); flex: none; }
  .brand__name {
    color: var(--brown); font-size: 19px; font-weight: 400; line-height: 1.25; width: 200px;
  }
  .divider {
    position: absolute; left: 318px; top: 118px; width: 2px; height: 128px; background: var(--brown);
  }
  .contact { position: absolute; left: 340px; top: 118px; }
  .contact__name {
    color: var(--brown); font-size: 27px; font-weight: 800; letter-spacing: 0.3px; margin-bottom: 14px;
  }
  .contact__row {
    display: flex; align-items: center; gap: 8px;
    color: var(--ink); font-size: 21px; line-height: 30px;
  }
  .contact__icon { width: 16px; height: 16px; flex: none; }
</style>
</head>
<body>
<main class="canvas">

  <section class="card card--back" aria-label="Card back">
    <div class="back-mark">
      <span class="back-mark__dot"></span>
      <span class="back-mark__name">Wexcombe Educational Group</span>
    </div>
    <p class="regions">
      <span>Australia</span><span class="regions__sep"></span>
      <span>South East Asia</span><span class="regions__sep"></span>
      <span>USA</span>
    </p>
  </section>

  <section class="card card--front" aria-label="Card front">
    <div class="brand">
      <span class="brand__dot"></span>
      <span class="brand__name">Wexcombe Educational Group</span>
    </div>
    <div class="divider"></div>
    <div class="contact">
      <h1 class="contact__name">Daniel Wexcombe</h1>
      <p class="contact__row">
        <svg class="contact__icon" viewBox="0 0 16 16" aria-hidden="true">
          <path d="M3 1.5l3 3-1.6 1.8c.9 1.9 2.4 3.4 4.3 4.3L10.5 9l3 3-1.8 2.2C6.5 14 2 9.5 1.8 4.3z" fill="var(--lime)"/>
        </svg>
        (03) 9417 2608
      </p>
      <p class="contact__row">
        <svg class="contact__icon" viewBox="0 0 16 16" aria-hidden="true">
          <rect x="1" y="3.5" width="14" height="9" rx="1" fill="var(--lime)"/>
          <path d="M1.5 4l6.5 5 6.5-5" fill="none" stroke="var(--white)" stroke-width="1.2"/>
        </svg>
        info@corvantela.com.au
      </p>
      <p class="contact__row">
        <svg class="contact__icon" viewBox="0 0 16 16" aria-hidden="true">
          <circle cx="8" cy="8" r="7" fill="var(--lime)"/>
          <path d="M1 8h14M8 1c-3 3.5-3 10.5 0 14M8 1c3 3.5 3 10.5 0 14" fill="none" stroke="var(--white)" stroke-width="1"/>
        </svg>
        www.corvantela.com.au
      </p>
    </div>
  </section>

</main>
</body>
</html>
```